HARBOUR LANE DECOR

We need a web design for a new business based in Bonny Hills (NSW). We are a small retail outlet on the Mid North Coast (NSW, Australia) selling home wares, gifts, beach wear, artwork, and hampers etc. We would like to a few different samples if that's not too much trouble (e.g. black and white vs colour, e.g. "beach colours").
We would like the website to communicate that we are an affordable, local (community based) business, with customer satisfaction at the forefront of our mind. We have a strong customer service focus, and in addition to retail sales we are now looking to expand into the online hamper business.
We are open 7 days (except public holidays).
Note: We like the design / layout of the "Cork Pail 'N' Shelf Website" if you would like to compare www.corkpailnshelf.com.au

Industry/Entity Type

Business

```html
<!DOCTYPE html>
<html lang="en">
<head>
<meta charset="utf-8">
<title>Harbour Lane Decor</title>
<link rel="stylesheet" href="https://fonts.googleapis.com/css2?family=Source+Sans+3:wght@400;600;700&display=swap">
<style>
  :root {
    --stage: #ebebeb;
    --page: #ffffff;
    --plum: #a0708f;
    --plum-text: #8a5a7a;
    --mint: #c2ebe0;
    --rose: #d098a8;
    --button: #b86e8a;
    --ink: #333333;
    --white: #ffffff;
    --logo-dot: #c8ece2;
  }
  * { box-sizing: border-box; margin: 0; padding: 0; }
  html, body { width: 1200px; height: 1000px; overflow: hidden; background: var(--page); }
  body { position: relative; font-family: "Source Sans 3", Arial, sans-serif; color: var(--ink); }

  .stage { position: absolute; left: 77px; top: 0; width: 1045px; height: 1000px; background: var(--stage); }
  .page { position: absolute; left: 160px; top: 20px; width: 880px; height: 952px; background: var(--page); }

  /* header */
  .site-header { position: absolute; left: 0; top: 0; width: 880px; height: 66px; }
  .brand-dot { position: absolute; left: 4px; top: 4px; width: 56px; height: 56px; border-radius: 50%; background: var(--logo-dot); }
  .brand-name { position: absolute; left: 114px; top: 14px; font-size: 17px; font-weight: 400; letter-spacing: 0.6px; color: #111; }
  .brand-tagline { position: absolute; left: 95px; top: 37px; font-size: 12.5px; color: #111; }
  .main-nav { position: absolute; left: 540px; top: 0; height: 66px; display: flex; }
  .main-nav a { display: flex; align-items: center; justify-content: center; height: 66px; font-size: 9px; letter-spacing: 0.4px; text-decoration: none; color: var(--plum-text); }
  .main-nav a.active { background: var(--plum); color: var(--white); font-weight: 600; width: 58px; }
  .nav-about { width: 64px; }
  .nav-services { width: 70px; }
  .nav-gallery { width: 76px; }
  .nav-contact { width: 70px; }
  .header-rule { position: absolute; left: 0; top: 66px; width: 880px; height: 4px; background: var(--plum); }

  /* hero */
  .hero-photo { position: absolute; left: 21px; top: 77px; width: 838px; height: 326px;
    background: linear-gradient(180deg, #d84a3a 0%, #2e6fa8 14%, #efefe8 22%, #c9c2b0 55%, #3ba8a0 75%, #e3d8c6 100%); }

  /* feature cards */
  .feature-card { position: absolute; top: 446px; width: 272px; height: 236px; background: var(--mint); }
  .card-one { left: 19px; }
  .card-two { left: 305px; }
  .card-three { left: 588px; }
  .card-photo { position: absolute; left: 16px; top: 24px; width: 221px; height: 110px; }
  .card-two .card-photo, .card-two .card-text, .card-two .read-more { left: 13px; }
  .card-three .card-photo, .card-three .card-text, .card-three .read-more { left: 14px; }
  .card-one .card-photo { background: linear-gradient(135deg, #e6e1d4, #d4913a 55%, #4b8a3c); }
  .card-two .card-photo { background: linear-gradient(180deg, #e9e4da, #c94a4a 45%, #3aa0a0 80%, #e6dfce); }
  .card-three .card-photo { background: linear-gradient(135deg, #c8b89c, #efece2 50%, #b84a4a 85%); }
  .card-text { position: absolute; left: 16px; top: 149px; width: 232px; font-size: 6.6px; line-height: 9.3px; color: var(--ink); }
  .card-two .card-text, .card-three .card-text { top: 145px; }
  .read-more { position: absolute; left: 16px; top: 219px; width: 67px; height: 22px; background: var(--button); color: #f3e6ec; font-size: 9.5px; display: flex; align-items: center; justify-content: center; text-decoration: none; }
  .read-more { top: 199px; }

  /* testimonial + contact */
  .testimonials { position: absolute; left: 19px; top: 727px; width: 558px; height: 183px; background: var(--rose); color: var(--white); padding: 11px 16px; }
  .testimonials h2 { font-size: 19px; font-weight: 400; letter-spacing: 0.2px; margin-bottom: 20px; }
  .testimonials p { font-size: 13.4px; line-height: 16.6px; width: 450px; }
  .testimonials .quote-source { margin-top: 16px; }
  .testimonials strong { font-weight: 600; display: block; }

  .contact-panel { position: absolute; left: 587px; top: 727px; width: 273px; height: 183px; background: var(--rose); color: var(--white); padding: 12px 15px; }
  .contact-panel h3 { font-size: 14.5px; font-weight: 400; margin-bottom: 15px; }
  .contact-panel address { font-style: normal; font-size: 10.8px; line-height: 13.5px; }
  .contact-panel .email { font-weight: 700; }
  .contact-panel .phones { font-size: 10.8px; margin-top: 13px; }
</style>
</head>
<body>
  <div class="stage"></div>
  <main class="page">
    <header class="site-header">
      <span class="brand-dot"></span>
      <div class="brand-name">Harbour Lane Decor</div>
      <div class="brand-tagline">home ware . kitchen ware . linen . gifts</div>
      <nav class="main-nav">
        <a class="active" href="#">HOME</a>
        <a class="nav-about" href="#">ABOUT</a>
        <a class="nav-services" href="#">SERVICES</a>
        <a class="nav-gallery" href="#">GALLERY</a>
        <a class="nav-contact" href="#">CONTACT</a>
      </nav>
    </header>
    <div class="header-rule"></div>

    <div class="hero-photo" role="img" aria-label="Shop interior with colourful cushions above white shelving holding folded towels, glassware and mugs"></div>

    <section class="feature-card card-one">
      <div class="card-photo" role="img" aria-label="Display of bright ceramic plates, jugs and bowls with artwork on the wall"></div>
      <p class="card-text">Lorem ipsum dolor sit amet, consectetur adipisicing elit, sed do eiusmod tempor incididunt ut labore et dolore magna aliqua. Duis aute irure dolor in reprehenderit in voluptate velit esse cillum dolore eu fugiat nulla pariatur.</p>
      <a class="read-more" href="#">Read More</a>
    </section>
    <section class="feature-card card-two">
      <div class="card-photo" role="img" aria-label="Shelving wall with cushions, linen and homewares"></div>
      <p class="card-text">Lorem ipsum dolor sit amet, consectetur adipisicing elit, sed do eiusmod tempor incididunt ut labore et dolore magna aliqua. Duis aute irure dolor in reprehenderit in voluptate velit esse cillum dolore eu fugiat nulla pariatur.</p>
      <a class="read-more" href="#">Read More</a>
    </section>
    <section class="feature-card card-three">
      <div class="card-photo" role="img" aria-label="Wide view of the store floor with shelves and cushions"></div>
      <p class="card-text">Lorem ipsum dolor sit amet, consectetur adipisicing elit, sed do eiusmod tempor incididunt ut labore et dolore magna aliqua. Duis aute irure dolor in reprehenderit in voluptate velit esse cillum dolore eu fugiat nulla pariatur.</p>
      <a class="read-more" href="#">Read More</a>
    </section>

    <section class="testimonials">
      <h2>WHAT PEOPLE SAY ABOUT US</h2>
      <p>Lorem ipsum dolor sit amet, consectetur adipisicing elit, sed in reprehenderit adipisicing elit, sed in reprehenderit in voluptate velit esse cillum dolore eu fugiat nulla pariatur.totam rem aperiam, eaque ipsa quae ab illo inventore veritatis et quasi architecto beatae vitae dicta sunt explicabo.</p>
      <p class="quote-source"><strong>consectetur adipisicing elit</strong>voluptate velit esse cillum dolore eu</p>
    </section>

    <aside class="contact-panel">
      <h3>Tessa Marlowe &amp; Renee Calder</h3>
      <address>
        5/14 Wattlebird Cres<br>
        Pelican Point NSW 2449<br>
        <span class="email">harbourlane318@mailbox.com</span>
      </address>
      <p class="phones">0491 570 156 &nbsp;&nbsp; 0491 570 110</p>
    </aside>
  </main>
</body>
</html>
```